Creative Businesss Card desgin!

Create a business card for our business Gleam window cleaning!
We are open to creative ideas as long as it maintains a professional image.

Target Market(s)

Small Commercial window cleaning clients including car dealerships, strata manager, cafe

Industry/Entity Type

Window Cleaning

Contact Information for Business Card

Daniel Prescott
General Manager
Gleam Window Cleaning

daniel@gleamservices.com.au
pane-care-southbank.com.au
Ph: 1800 GET GLEAM
Mob: 0437 582 061

Colors
fbed22
0392cd

Requirements
Should not have
• Stock window cleaning/ squeegee graphics

```html
<!DOCTYPE html>
<html lang="en">
<head>
<meta charset="utf-8">
<title>Gleam Window Cleaning – Business Card</title>
<link rel="stylesheet" href="https://fonts.googleapis.com/css2?family=PT+Sans:wght@400;700&display=swap">
<style>
  :root {
    --page-bg: #e6e4e1;
    --card-blue: #0d6199;
    --brand-yellow: #f4ec22;
    --foil-silver: #b8c5d1;
    --text-white: #ffffff;
    --divider: rgba(255, 255, 255, 0.55);
    --card-shadow: 0 10px 28px rgba(0, 0, 0, 0.22);
  }
  * { box-sizing: border-box; }
  html, body {
    margin: 0;
    width: 1200px;
    height: 864px;
    overflow: hidden;
    background: var(--page-bg);
    font-family: "PT Sans", sans-serif;
  }
  .sheet {
    width: 1200px;
    height: 864px;
    display: flex;
    flex-direction: column;
    align-items: center;
    justify-content: center;
    gap: 44px;
  }
  .card {
    position: relative;
    width: 620px;
    height: 379px;
    background: var(--card-blue);
    box-shadow: var(--card-shadow);
    color: var(--text-white);
  }
  .brand-name {
    margin: 0;
    font-weight: 700;
    text-transform: uppercase;
    line-height: 0.9;
  }
  .brand-name .word { display: block; font-size: 78px; letter-spacing: 1px; }
  .brand-name .sub { display: block; font-size: 27px; letter-spacing: 0.5px; margin-top: 4px; }

  /* Card back */
  .card-back .brand-name {
    position: absolute;
    left: 120px;
    top: 84px;
    color: var(--foil-silver);
  }
  .card-back .website {
    position: absolute;
    left: 112px;
    top: 238px;
    font-size: 15px;
    color: var(--foil-silver);
    letter-spacing: 0.3px;
  }

  /* Card front */
  .card-front .brand-name {
    position: absolute;
    left: 62px;
    top: 128px;
    color: var(--brand-yellow);
  }
  .card-front .brand-name .word { font-size: 70px; }
  .card-front .brand-name .sub { font-size: 24px; }
  .divider {
    position: absolute;
    left: 336px;
    top: 104px;
    width: 1px;
    height: 172px;
    background: var(--divider);
  }
  .contact {
    position: absolute;
    left: 356px;
    top: 112px;
  }
  .person-name {
    margin: 0;
    color: var(--brand-yellow);
    font-weight: 700;
    font-size: 22px;
    text-transform: uppercase;
    line-height: 1.05;
  }
  .person-title {
    margin: 0 0 6px;
    color: var(--text-white);
    font-weight: 700;
    font-size: 17px;
    text-transform: uppercase;
  }
  .company {
    margin: 0 0 6px;
    font-size: 16px;
  }
  .contact-list {
    list-style: none;
    margin: 0;
    padding: 0;
    font-size: 16px;
    line-height: 1.4;
  }
  .contact-list li {
    display: flex;
    align-items: center;
    gap: 9px;
  }
  .contact-list svg {
    width: 14px;
    height: 14px;
    flex: none;
    fill: var(--brand-yellow);
  }
</style>
</head>
<body>
<main class="sheet">
  <section class="card card-back" aria-label="Business card back">
    <h1 class="brand-name"><span class="word">Gleam</span><span class="sub">Window Cleaning</span></h1>
    <p class="website">www.pane-care-southbank.com.au</p>
  </section>

  <section class="card card-front" aria-label="Business card front">
    <h2 class="brand-name"><span class="word">Gleam</span><span class="sub">Window Cleaning</span></h2>
    <div class="divider"></div>
    <div class="contact">
      <p class="person-name">Daniel Prescott</p>
      <p class="person-title">General Manager</p>
      <p class="company">Gleam Window Cleaning</p>
      <ul class="contact-list">
        <li>
          <svg viewBox="0 0 16 16" aria-hidden="true"><path d="M1 5c0-2 3-3 7-3s7 1 7 3v1.5h-3.5V5H4.5v1.5H1zM3.5 7.5h9l1.5 7H2z"/></svg>
          1800 GET GLEAM
        </li>
        <li>
          <svg viewBox="0 0 16 16" aria-hidden="true"><path d="M4.5 1h7v14h-7zM6 3v9h4V3z"/></svg>
          0437 582 061
        </li>
        <li>
          <svg viewBox="0 0 16 16" aria-hidden="true"><path d="M1 3.5h14v9H1zM2.5 5l5.5 4 5.5-4v-.2H2.5z"/></svg>
          daniel@gleamservices.com.au
        </li>
        <li>
          <svg viewBox="0 0 16 16" aria-hidden="true"><path d="M8 1a7 7 0 1 0 0 14A7 7 0 0 0 8 1zm-1 2.2v2.3H4.4A5 5 0 0 1 7 3.2zm2 0a5 5 0 0 1 2.6 2.3H9zM3.2 7.5H7v1H3.2zm5.8 0h3.8v1H9zM4.4 10.5H7v2.3a5 5 0 0 1-2.6-2.3zm4.6 0h2.6A5 5 0 0 1 9 12.8z"/></svg>
          pane-care-southbank.com.au
        </li>
      </ul>
    </div>
  </section>
</main>
</body>
</html>
```